Gather the Orchard Gala Graphic Design

I’m seeking a professional graphic designer experienced in event branding to create a cohesive suite of materials for our third annual fundraising gala, “Gather the Orchard.” This year's theme is " An Evening in Linen to Gather the Orchard" Need to design collateral for website, social media and email blasts.
Target Market(s)
Affluent gala attendees
Industry/Entity Type
Fundraising / Charity / Outdoors / Sports
Font styles to use
Decorative
Script
Colors
0054AA
0677BA
7BADD7
CADEEF
E8F1F8
0094D4
00A9DD
6FCCEA
C7EBF8
E9F6FB
00AB8E
00BBA5
67D7C9
C6EFE9
E9F9F6
6B429C
8869AF
B7A5CE
E3DAEB
F3F0F8

```html
<!DOCTYPE html>
<html lang="en">
<head>
<meta charset="UTF-8">
<title>An Evening in Linen to Gather the Orchard</title>
<link href="https://fonts.googleapis.com/css2?family=Playfair+Display:wght@700;900&family=Great+Vibes&family=Poppins:wght@400;600;700&family=Oswald:wght@500&display=swap" rel="stylesheet">
<style>
  :root {
    --night: #0b1a3a;
    --deep-blue: #13305c;
    --sea-blue: #1e4a6e;
    --teal-dark: #0e6f68;
    --teal: #00AB8E;
    --teal-bright: #00BBA5;
    --teal-soft: #67D7C9;
    --teal-pale: #C6EFE9;
    --sky-pale: #C7EBF8;
    --white: #ffffff;
    --pill-text: #0a8f80;
  }
  * { margin: 0; padding: 0; box-sizing: border-box; }
  html, body { width: 1200px; height: 1200px; overflow: hidden; background: var(--night); }
  .gala-poster {
    position: relative;
    width: 1200px;
    height: 1200px;
    overflow: hidden;
    font-family: "Poppins", sans-serif;
    color: var(--white);
    text-align: center;
  }
  .scene-backdrop {
    position: absolute; inset: 0;
    background:
      radial-gradient(ellipse at 50% 20%, rgba(60,90,150,0.35), transparent 60%),
      linear-gradient(180deg, var(--night) 0%, var(--deep-blue) 45%, var(--sea-blue) 58%, var(--teal-dark) 80%, #0a7a6f 100%);
  }
  .line { position: absolute; left: 0; width: 100%; white-space: nowrap; }
  .title-top {
    top: 228px;
    font-family: "Playfair Display", serif;
    font-weight: 700;
    font-size: 84px;
    letter-spacing: 3px;
    line-height: 1;
    transform: scaleX(0.8);
  }
  .title-main {
    top: 268px;
    height: 440px;
    display: flex;
    justify-content: center;
    overflow: visible;
  }
  .title-main span {
    display: block;
    flex: none;
    font-family: "Playfair Display", serif;
    font-weight: 900;
    font-size: 500px;
    line-height: 0.85;
    transform: scaleX(0.56);
    transform-origin: 50% 50%;
    background: linear-gradient(180deg, #ffffff 0%, #f1f5fb 45%, rgba(200,215,235,0.55) 80%, rgba(200,215,235,0.1) 100%);
    -webkit-background-clip: text;
    background-clip: text;
    color: transparent;
  }
  .title-script {
    top: 606px;
    font-family: "Great Vibes", cursive;
    font-size: 104px;
    line-height: 1;
    color: var(--sky-pale);
  }
  .intro {
    top: 744px;
    font-size: 24px;
    font-weight: 400;
  }
  .cause-button {
    position: absolute;
    left: 428px; top: 789px;
    width: 344px; height: 80px;
    border-radius: 12px;
    background: linear-gradient(180deg, var(--teal-bright), var(--teal));
    box-shadow: 0 0 18px rgba(103,215,201,0.55);
    font-family: "Great Vibes", cursive;
    font-size: 58px;
    line-height: 80px;
  }
  .venue-name { top: 890px; font-size: 24px; }
  .event-date { top: 925px; font-size: 40px; font-weight: 600; }
  .event-time { top: 970px; font-size: 31px; font-weight: 600; }
  .event-address { top: 1015px; font-size: 30px; font-weight: 600; }
  .dress-code {
    position: absolute;
    left: 391px; top: 1069px;
    width: 418px; height: 31px;
    border-radius: 16px;
    background: var(--white);
    color: var(--pill-text);
    font-family: "Oswald", sans-serif;
    font-weight: 500;
    font-size: 18px;
    letter-spacing: 1.5px;
    line-height: 31px;
  }
  .ticket-band {
    position: absolute;
    left: 0; top: 1115px;
    width: 1200px; height: 50px;
    background: linear-gradient(90deg, rgba(198,239,233,0.4) 0%, #eefaf8 18%, #eefaf8 82%, rgba(198,239,233,0.4) 100%);
    color: var(--teal);
    font-weight: 700;
    font-size: 29px;
    line-height: 50px;
  }
</style>
</head>
<body>
  <main class="gala-poster">
    <div class="scene-backdrop" role="img" aria-label="Night sky full of stars above a calm teal sea, with a tall iron-framed tower casting a beam of light"></div>

    <div class="line title-top">AN EVENING IN</div>
    <div class="line title-main"><span>LINEN</span></div>
    <div class="line title-script">to Gather the Orchard</div>

    <p class="line intro">Join us for an unforgettable evening as we celebrate the ongoing efforts to</p>
    <div class="cause-button">Preserve</div>
    <p class="line venue-name">Marlow Ridge Orchard!</p>
    <p class="line event-date">NOVEMBER 15, 2025</p>
    <p class="line event-time">COCKTAILS AT 5:00 PM</p>
    <p class="line event-address">Cedar Hollow Green - 4120 Meadow Lane Rd, Fairhaven</p>
    <div class="dress-code">COCKTAIL ATTIRE – WHITE AND SILVER</div>
    <div class="ticket-band">Get Your Tickets Today!</div>
  </main>
</body>
</html>
```